Innovative Bitcoin Powerpoint Presentation

I have constructred most of the data for a 15 page powerpoint presentation on an innovative bitcoin idea that provides access to fiat currency with bitcoin hodlings

I need this to look great as a first blush to potential investors

Reason: updated deck and name

Target Market(s)

Venture Capital firms and private equity firms

Requirements
Must have
• Fun, innovateive deck, very clean
Should not have
• any generic feel - no templates

```html
<!DOCTYPE html>
<html lang="en">
<head>
<meta charset="utf-8">
<title>Higher Rate of Innovation</title>
<link rel="stylesheet" href="https://fonts.googleapis.com/css2?family=Roboto+Condensed:wght@700&family=Open+Sans:wght@400;600&display=swap">
<style>
  :root {
    --orange-deep: #f39a1c;
    --orange-mid: #f8b232;
    --orange-light: #fcd073;
    --page-bg: #f3f3f3;
    --ink: #111111;
    --text-grey: #3b3f45;
    --axis: #333333;
    --band-grey: #8d8d8d;
    --band-orange: #f4891f;
    --bar-gray: #909090;
    --bar-dark: #6f6f6f;
    --bar-gold: #f0ad30;
    --bar-cream: #fde59a;
    --bar-amber: #fdbf50;
    --bar-sand: #efb75a;
    --bar-yellow: #fbb939;
    --white: #ffffff;
  }
  html, body {
    margin: 0;
    padding: 0;
    overflow: hidden;
  }
  .slide {
    position: relative;
    width: 1200px;
    height: 900px;
    overflow: hidden;
    background: radial-gradient(circle at 80% 30%, #fafafa 0%, var(--page-bg) 55%, #ececec 100%);
    font-family: "Open Sans", Arial, sans-serif;
  }
  .slide-header {
    position: absolute;
    left: 0; top: 0;
    width: 1200px; height: 112px;
    background:
      radial-gradient(ellipse at 32% 90%, rgba(255,236,170,0.85) 0%, rgba(255,236,170,0) 35%),
      radial-gradient(ellipse at 70% 20%, rgba(255,220,130,0.7) 0%, rgba(255,220,130,0) 40%),
      linear-gradient(90deg, var(--orange-light) 0%, var(--orange-mid) 45%, var(--orange-deep) 100%);
  }
  .slide-title {
    position: absolute;
    left: 32px; top: 28px;
    margin: 0;
    font-family: "Roboto Condensed", "Arial Narrow", sans-serif;
    font-weight: 700;
    font-size: 42px;
    line-height: 1;
    color: var(--ink);
  }
  .brand-name {
    position: absolute;
    right: 14px; top: 30px;
    font-family: "Roboto Condensed", "Arial Narrow", sans-serif;
    font-weight: 700;
    font-size: 48px;
    line-height: 1;
    color: var(--white);
  }
  .slide-lead {
    position: absolute;
    left: 72px; top: 175px;
    margin: 0;
    font-weight: 600;
    font-size: 22px;
    color: var(--text-grey);
  }
  .chart-art {
    position: absolute;
    left: 0; top: 0;
  }
  .axis-label {
    position: absolute;
    font-size: 17px;
    color: var(--text-grey);
    white-space: nowrap;
    line-height: 1;
  }
  .y-label { left: 70px; }
  .x-label { top: 741px; }
</style>
</head>
<body>
<main class="slide">
  <header class="slide-header">
    <h1 class="slide-title">Higher Rate of Innovation</h1>
    <div class="brand-name">LEDGERLY</div>
  </header>

  <p class="slide-lead">Lorem ipsum dolor sit ipsum Lorem ipsum dolor sit ipsum Lorem ipsum Lorem ipsum</p>

  <svg class="chart-art" width="1200" height="900" viewBox="0 0 1200 900" aria-label="Bar chart">
    <g class="bars">
      <rect x="273" y="574" width="50" height="143" fill="var(--bar-gray)"/>
      <rect x="333" y="460" width="63" height="257" fill="var(--bar-gold)"/>
      <rect x="412" y="507" width="60" height="210" fill="var(--bar-cream)"/>
      <rect x="486" y="591" width="60" height="126" fill="var(--bar-amber)"/>
      <rect x="564" y="679" width="64" height="38" fill="var(--bar-sand)"/>
      <rect x="642" y="705" width="74" height="12" fill="var(--bar-dark)"/>
      <rect x="726" y="315" width="62" height="402" fill="var(--bar-gold)"/>
      <rect x="801" y="678" width="66" height="39" fill="var(--bar-cream)"/>
      <rect x="879" y="697" width="63" height="20" fill="var(--bar-yellow)"/>
    </g>
    <g class="axes" stroke="var(--axis)" stroke-width="1.5">
      <line x1="273" y1="277" x2="273" y2="717"/>
      <line x1="273" y1="717" x2="1032" y2="717"/>
    </g>
    <g class="footer-bands">
      <polygon points="0,858 858,858 834,900 0,900" fill="var(--band-grey)"/>
      <polygon points="878,843 1200,843 1200,900 842,900" fill="var(--band-orange)"/>
    </g>
  </svg>

  <span class="axis-label y-label" style="top:292px">Lorem ipsum text here</span>
  <span class="axis-label y-label" style="top:362px">Lorem ipsum text here</span>
  <span class="axis-label y-label" style="top:454px">Lorem ipsum text here</span>
  <span class="axis-label y-label" style="top:570px">Lorem ipsum text here</span>
  <span class="axis-label y-label" style="top:702px">Lorem ipsum text here</span>

  <span class="axis-label x-label" style="left:270px">Lorem ipsum text here</span>
  <span class="axis-label x-label" style="left:532px">Lorem ipsum text here</span>
  <span class="axis-label x-label" style="left:849px">Lorem ipsum text here</span>
</main>
</body>
</html>
```